Veterinary Clinic Letterhead - Ridgeview Veterinary Surgery

We need a letterhead design for an established Veterinary Clinic in Mareeba called Ridgeview Veterinary Surgery. We are a moderate sized mixed animal veterinary clinic offering a wide variety of veterinary services. The design should use the same colour pattern as those in the logos supplied. The design should also include our address (48 Tulloch Road, Ashford Vale, Queensland, 4871), phone number (07 4158 6734), email (admin@ridgeviewvets.com.au), website (www.ridgeviewvets.com.au) and our opening hours (8am to 6pm Monday to Friday and 9am to 1pm Saturday).
Target Market(s)
Pet owners
Industry/Entity Type
Veterinary
Requirements
Must have
- The logo or modification of it, business address, opening hours, website, phone number and email address

```html
<!DOCTYPE html>
<html lang="en">
<head>
<meta charset="utf-8">
<title>Ridgeview Veterinary Surgery — Letterhead</title>
<link href="https://fonts.googleapis.com/css2?family=Montserrat:wght@400;500&display=swap" rel="stylesheet">
<style>
  :root {
    --navy: #1c2c4b;
    --paper: #ffffff;
    --backdrop: #e9e7e4;
    --faint: #ebebef;
    --ink: #1c2438;
  }
  html, body {
    margin: 0;
    width: 1200px;
    height: 900px;
    overflow: hidden;
    background: var(--backdrop);
    font-family: "Montserrat", sans-serif;
    color: var(--ink);
  }
  .letterhead {
    position: absolute;
    left: 275px;
    top: 31px;
    width: 650px;
    height: 838px;
    background: var(--paper);
    box-shadow: 0 4px 14px rgba(0,0,0,0.15);
    overflow: hidden;
  }
  .side-band {
    position: absolute;
    top: 0;
    right: 0;
    width: 90px;
    height: 100%;
  }
  .brand {
    position: absolute;
    left: 0;
    width: 560px;
    top: 52px;
    display: flex;
    justify-content: center;
    align-items: center;
    gap: 10px;
  }
  .brand-dot {
    width: 22px;
    height: 22px;
    border-radius: 50%;
    background: var(--navy);
  }
  .brand-name {
    font-size: 15px;
    font-weight: 500;
    letter-spacing: 0.06em;
    color: var(--navy);
    text-transform: uppercase;
    line-height: 1;
  }
  .faint-name {
    position: absolute;
    left: 0;
    width: 560px;
    top: 400px;
    text-align: center;
    font-size: 24px;
    font-weight: 500;
    color: var(--faint);
    letter-spacing: 0.06em;
    text-transform: uppercase;
  }
  .contact-footer {
    position: absolute;
    left: 60px;
    width: 440px;
    top: 763px;
    font-size: 10.5px;
    text-align: center;
    color: var(--ink);
    letter-spacing: 0.02em;
  }
  .contact-footer .address,
  .contact-footer .hours {
    margin: 0;
    line-height: 1.1;
  }
  .contact-footer .contact-row {
    margin: 6px 0;
    padding: 6px 0;
    border-top: 1px solid var(--navy);
    border-bottom: 1px solid var(--navy);
    display: flex;
    justify-content: space-between;
    align-items: center;
    line-height: 1.1;
  }
  .contact-item {
    display: inline-flex;
    align-items: center;
    gap: 4px;
    white-space: nowrap;
  }
  .contact-item svg { width: 10px; height: 10px; fill: var(--navy); }
</style>
</head>
<body>
  <main class="letterhead">
    <svg class="side-band" viewBox="0 0 90 838" preserveAspectRatio="none" aria-hidden="true">
      <path d="M50 0 C70 280 20 560 40 838 L90 838 L90 0 Z" fill="var(--navy)"/>
    </svg>

    <header class="brand">
      <span class="brand-dot"></span>
      <span class="brand-name">Ridgeview Veterinary Surgery</span>
    </header>

    <div class="faint-name">Ridgeview Veterinary Surgery</div>

    <footer class="contact-footer">
      <p class="address">48 Tulloch Road, Ashford Vale, Queensland, 4871</p>
      <div class="contact-row">
        <span class="contact-item">
          <svg viewBox="0 0 24 24"><path d="M6.6 10.8a15 15 0 0 0 6.6 6.6l2.2-2.2c.3-.3.7-.4 1-.2 1.1.4 2.3.6 3.6.6.6 0 1 .4 1 1V20c0 .6-.4 1-1 1A17 17 0 0 1 3 4c0-.6.4-1 1-1h3.5c.6 0 1 .4 1 1 0 1.3.2 2.5.6 3.6.1.3 0 .7-.2 1z"/></svg>
          07 4158 6734
        </span>
        <span class="contact-item">
          <svg viewBox="0 0 24 24"><path d="M2 5h20v2l-10 6L2 7z M2 9l10 6 10-6v10H2z"/></svg>
          admin@ridgeviewvets.com.au
        </span>
        <span class="contact-item">
          <svg viewBox="0 0 24 24"><circle cx="12" cy="12" r="10"/><path d="M2 12h20M12 2c3 3 3 17 0 20M12 2c-3 3-3 17 0 20" stroke="#fff" stroke-width="1.5" fill="none"/></svg>
          www.ridgeviewvets.com.au
        </span>
      </div>
      <p class="hours">8am to 6pm Monday to Friday and 9am to 1pm Saturday</p>
    </footer>
  </main>
</body>
</html>
```